Bright Path Crest Oak Realty yard sign Logo

UPDATE Design logo for Realty yard sign. 24x24 diamond or 36x24 Rectangle.
Open to all ideas. We are a discount firm but want to project a high end feel. We provide 100% of all services and extensive marketing for 1/2 the fee.
The following info must be on sign
BRIGHT PATH CREST (OR 1/3) OAK REALTY
Tomas Reyne 555-0147
CrestoakQX.com

Target Market(s)

home sellers and buyers

Industry/Entity Type

Real Estate yard sign please see sign attached in gif

Logo Text

Bright Path Crest Oak Realty OR (1/3 IN PLACE OF CREST)

Requirements
Must have
• BRIGHT PATH CREST (OR 1/3) OAK REALTY Tomas Reyne 555-0147 CrestoakQX.com FOR SALE (optional)

```html
<!DOCTYPE html>
<html lang="en">
<head>
<meta charset="utf-8">
<title>Bright Path Crest Oak Realty – For Sale Yard Sign</title>
<link rel="stylesheet" href="https://fonts.googleapis.com/css2?family=Montserrat:wght@500;600;900&display=swap">
<style>
  :root {
    --page-bg: #ececec;
    --sign-bg: #e3e6f2;
    --navy-deep: #25216a;
    --navy-royal: #2b3b98;
    --sky-blue: #1a7cc0;
    --ink: #111111;
    --white: #ffffff;
    --photo-sky: #b9bfdc;
    --photo-house: #4a5585;
    --photo-ground: #2d3556;
  }
  html, body {
    margin: 0;
    padding: 0;
    width: 1200px;
    height: 1200px;
    overflow: hidden;
    background: var(--page-bg);
  }
  .canvas {
    width: 1200px;
    height: 1200px;
    display: flex;
    align-items: center;
    justify-content: center;
  }
  .yard-sign {
    display: block;
    width: 742px;
    height: 1110px;
    box-shadow: 0 4px 18px rgba(0,0,0,0.08);
  }
  .sign-bg { fill: var(--sign-bg); }
  .shape-navy { fill: var(--navy-deep); }
  .shape-royal { fill: var(--navy-royal); }
  .shape-sky { fill: var(--sky-blue); }
  .headline {
    font-family: 'Montserrat', sans-serif;
    font-weight: 900;
    font-size: 67px;
    fill: var(--ink);
    letter-spacing: 0.5px;
  }
  .firm-name {
    font-family: 'Montserrat', sans-serif;
    font-weight: 600;
    font-size: 29px;
    fill: var(--ink);
  }
  .agent-name {
    font-family: 'Montserrat', sans-serif;
    font-weight: 500;
    font-size: 20px;
    fill: var(--ink);
  }
  .agent-phone {
    font-family: 'Montserrat', sans-serif;
    font-weight: 500;
    font-size: 19px;
    fill: var(--ink);
  }
  .brand-name {
    font-family: 'Montserrat', sans-serif;
    font-weight: 600;
    font-size: 17px;
    fill: var(--white);
  }
  .web-address {
    font-family: 'Montserrat', sans-serif;
    font-weight: 500;
    font-size: 21px;
    fill: var(--white);
  }
  .icon-line { fill: none; stroke: var(--white); stroke-width: 1.6; }
  .icon-phone { fill: var(--ink); }
  .rule { fill: var(--ink); }
</style>
</head>
<body>
<main class="canvas">
  <svg class="yard-sign" viewBox="0 0 705 1055" xmlns="http://www.w3.org/2000/svg" aria-label="For Sale yard sign for Bright Path Crest Oak Realty">
    <defs>
      <linearGradient id="houseDusk" x1="0" y1="0" x2="0" y2="1">
        <stop offset="0" stop-color="#c5c8e2"/>
        <stop offset="0.45" stop-color="#5d6794"/>
        <stop offset="0.8" stop-color="#3a4470"/>
        <stop offset="1" stop-color="#2d3556"/>
      </linearGradient>
      <linearGradient id="houseEvening" x1="0" y1="0" x2="0" y2="1">
        <stop offset="0" stop-color="#d2c9e0"/>
        <stop offset="0.4" stop-color="#4f5a8c"/>
        <stop offset="0.85" stop-color="#5a6180"/>
        <stop offset="1" stop-color="#40486a"/>
      </linearGradient>
    </defs>

    <!-- background -->
    <rect class="sign-bg" x="0" y="0" width="705" height="1055"/>

    <!-- top geometric bands -->
    <polygon class="shape-navy" points="0,0 178,0 0,178"/>
    <polygon class="shape-sky" points="192,0 640,0 416,224"/>
    <polygon class="shape-navy" points="658,0 683,0 165,518 152,505"/>

    <!-- photo panels -->
    <polygon role="img" aria-label="Photo of a two-storey suburban house at dusk with lit windows and a lawn"
             fill="url(#houseDusk)" points="0,110 165,23 417,275 165,527 0,362"/>
    <polygon role="img" aria-label="Photo of a grey family home with a double garage in evening light"
             fill="url(#houseEvening)" points="572,178 705,311 705,549 572,682 320,430"/>

    <!-- lower geometric bands -->
    <polygon class="shape-navy" points="705,585 705,610 260,1055 235,1055"/>
    <polygon class="shape-sky" points="532,803 705,630 705,975"/>
    <polygon class="shape-royal" points="520,815 705,1000 705,1055 280,1055"/>

    <!-- headline & firm name -->
    <text class="headline" x="42" y="687">FOR SALE</text>
    <text class="firm-name" x="44" y="749">BRIGHT PATH CREST</text>
    <text class="firm-name" x="44" y="800">( OR 1/3 )</text>
    <text class="firm-name" x="44" y="852">OAK REALTY</text>

    <!-- agent -->
    <text class="agent-name" x="50" y="985">Tomas Reyne</text>
    <rect class="rule" x="42" y="995" width="124" height="5"/>
    <path class="icon-phone" d="M48,1022 c1.5,-1.2 3.2,-1.2 4,0 l2.2,3.2 c0.6,0.9 0.3,1.9 -0.6,2.5 l-1.3,0.9 c1,2.4 2.8,4.3 5.2,5.3 l0.9,-1.3 c0.6,-0.9 1.7,-1.2 2.6,-0.6 l3.2,2.2 c1.1,0.8 1.1,2.5 0,4 c-1.6,2 -4,2.4 -6.4,1.2 c-4.6,-2.3 -8.2,-5.9 -10.4,-10.5 c-1.2,-2.5 -0.6,-5 0.6,-6.9 z"/>
    <text class="agent-phone" x="77" y="1037">555-0147</text>

    <!-- brand & web -->
    <text class="brand-name" x="672" y="988" text-anchor="end">Bright Path Crest Oak Realty</text>
    <g class="web-icon" transform="translate(468,1029)">
      <circle class="icon-line" cx="0" cy="0" r="11"/>
      <ellipse class="icon-line" cx="0" cy="0" rx="4.8" ry="11"/>
      <line class="icon-line" x1="-11" y1="0" x2="11" y2="0"/>
      <line class="icon-line" x1="-9.5" y1="-5.5" x2="9.5" y2="-5.5"/>
      <line class="icon-line" x1="-9.5" y1="5.5" x2="9.5" y2="5.5"/>
    </g>
    <text class="web-address" x="494" y="1036">CrestoakQX.com</text>
  </svg>
</main>
</body>
</html>
```